Kelvo Marine business card

We sell live saltwater fish and live corals
Kelvo Marine
7 Harlow Ct
Corvel, NJ. 08123
(856) 555-0147
Contact Information for Business Card
Kelvo Marine
7 Harlow Ct
Corvel, NJ. 08123
(856) 555-0147
Colors
Designer to choose colors to be used in the design.

```html
<!DOCTYPE html>
<html lang="en">
<head>
<meta charset="utf-8">
<title>Kelvo Marine — Business Card</title>
<link href="https://fonts.googleapis.com/css2?family=Cinzel:wght@700&display=swap" rel="stylesheet">
<style>
  :root {
    --page: #e9e9eb;
    --reef-light: #a99bd3;
    --reef-light-edge: #9c8cc9;
    --reef-deep: #3a3696;
    --reef-deep-mid: #47409f;
    --ink: #ffffff;
  }
  html, body {
    margin: 0;
    width: 1200px;
    height: 800px;
    overflow: hidden;
    background: var(--page);
  }
  .business-card {
    position: absolute;
    left: 180px;
    top: 160px;
    width: 840px;
    height: 480px;
    overflow: hidden;
  }
  .card-art {
    position: absolute;
    inset: 0;
    width: 100%;
    height: 100%;
  }
  .card-details {
    position: absolute;
    inset: 0;
    display: flex;
    flex-direction: column;
    align-items: center;
    justify-content: center;
    font-family: "Cinzel", "Times New Roman", serif;
    font-weight: 700;
    color: var(--ink);
    text-align: center;
    line-height: 1.05;
    padding-top: 6px;
  }
  .company-name { font-size: 52px; margin: 0 0 16px; }
  .address-line { font-size: 54px; margin: 0; white-space: nowrap; }
  .phone { font-size: 56px; margin: 16px 0 0; white-space: nowrap; }
</style>
</head>
<body>
  <div class="business-card">
    <svg class="card-art" viewBox="0 0 840 480" role="img" aria-label="Coral reef photograph with tropical fish, tinted purple, fills the card">
      <defs>
        <linearGradient id="reefLight" x1="0" y1="0" x2="0" y2="1">
          <stop offset="0" stop-color="var(--reef-light)"/>
          <stop offset="1" stop-color="var(--reef-light-edge)"/>
        </linearGradient>
        <radialGradient id="reefDeep" cx="0.5" cy="0.5" r="0.7">
          <stop offset="0" stop-color="var(--reef-deep)"/>
          <stop offset="1" stop-color="var(--reef-deep-mid)"/>
        </radialGradient>
      </defs>
      <rect class="reef-backdrop" width="840" height="480" fill="url(#reefLight)"/>
      <path class="wave-band" fill="url(#reefDeep)"
        d="M0,110 C10,50 80,20 140,45 C200,70 230,75 290,50 C360,20 410,20 470,50 C530,80 570,80 630,50 C690,20 740,20 790,45 C830,65 840,90 840,110
           L840,380 C830,420 790,440 740,420 C680,395 640,385 580,410 C520,440 470,445 410,420 C350,395 310,385 250,410 C190,440 140,445 80,420 C40,400 0,390 0,370 Z"/>
    </svg>
    <div class="card-details">
      <p class="company-name">Kelvo Marine</p>
      <p class="address-line">7 Harlow Ct</p>
      <p class="address-line">Corvel, NJ. 08123</p>
      <p class="phone">(856) 555-0147</p>
    </div>
  </div>
</body>
</html>
```